BROCHURE OR FLYER PLEASE

We need a brochure design for our company TV Surfacing Contractors Limited. Our website is www.tvsurfacing-demo.co.nz. We have rented a 3m permanent booth at the dwelling plans hub in central Auckland. Their website is: www.dwellingplans-demo.co.nz
We need to design and provide a company brochure outlining who we are, and the types of services we provide. Half of our flooring business is dedicated to basically Polished Concrete/Concrete Grinding; and the other half to resin and other floor toppings. We are based in Auckland, NZ and will be marketing to existing and new home owners essentially in Auckland. We want to contain concise information on our services and present this in a professional but sheik style. Housing in NZ is expensive so our brochure needs to be up market and user friendly. Polished concrete is more expensive that carpet so I feel it is important to list the benefits etc. I will attach our website and information regarding our products. We would like a double sided brochure. Our company colours are blue/red/black. I have attached some photo's you are welcome to use. Please refer to our website for more information www.tvsurfacing-demo.co.nz. Thank you.

Target Market(s)

Home Owners

Industry/Entity Type

Marketing

Requirements
Must have
• Company logo and contact details.

```html
<!DOCTYPE html>
<html lang="en">
<head>
<meta charset="utf-8">
<title>TV Surfacing Contractors – Brochure</title>
<link rel="stylesheet" href="https://fonts.googleapis.com/css2?family=Open+Sans:wght@400;600;700&family=Playfair+Display:wght@700&family=Dancing+Script:wght@600&family=Oswald:wght@600&display=swap">
<style>
  :root{
    --stage:#e8e8e8;
    --blue:#2b83cc;
    --blue-deep:#165a9e;
    --blue-band:#0f3f72;
    --gold:#ffe14a;
    --red:#e0262b;
    --ink:#1a1a1a;
    --paper:#fbfbfb;
    --muted:#444;
  }
  *{box-sizing:border-box;margin:0;padding:0}
  html,body{width:1200px;height:900px;overflow:hidden;background:var(--stage)}
  body{font-family:"Open Sans",Arial,sans-serif}
  .brochure{position:absolute;left:60px;top:70px;width:1080px;height:760px;display:flex;box-shadow:0 10px 30px rgba(0,0,0,.18)}
  .panel{width:360px;height:760px;position:relative}
  .panel--blue{background:linear-gradient(180deg,#3a95dc 0%,var(--blue) 45%,var(--blue-deep) 100%);color:#fff}
  .panel--middle{border-left:1px solid rgba(0,0,0,.12)}
  .panel--white{background:var(--paper);color:var(--ink);overflow:hidden}
  .panel-copy{position:relative;z-index:2;padding:34px 32px 0}
  .headline{text-align:center;font-weight:400;line-height:1.2}
  .headline .lead{display:block;font-size:18px;white-space:nowrap}
  .headline .gold{color:var(--gold);font-weight:700}
  .headline .serif{display:block;font-family:"Playfair Display",Georgia,serif;font-weight:700;font-size:21px;margin-top:2px}
  .body-copy{font-size:11.5px;line-height:1.45;margin-top:14px;text-align:center}
  .checks{display:flex;justify-content:space-between;margin-top:24px;font-size:12px;letter-spacing:.5px}
  .checks li{list-style:none;display:flex;align-items:center;gap:4px;color:#eaf4ff}
  .checks svg{width:22px;height:18px}
  .headline--right{text-align:center;line-height:1.2}
  .headline--right .light{display:block;font-weight:400;font-size:20px}
  .headline--right .bold{display:block;font-weight:700;font-size:20px;letter-spacing:.5px}
  .options-title{font-size:14px;font-weight:600;margin-top:14px}
  .options{margin-top:6px;font-size:11.5px;line-height:1.45;padding-left:14px}
  .options li{margin-bottom:2px}
  .scene{position:absolute;left:0;top:0;z-index:1;pointer-events:none}
  .social{position:absolute;left:22px;bottom:16px;z-index:3;display:flex;align-items:center;gap:7px;font-size:12px;color:#fff}
  .social i{width:14px;height:14px;border-radius:50%;background:#fff;display:inline-block}
  .about{padding:34px 30px 0}
  .about h2{color:var(--blue);font-size:16px;font-weight:700;letter-spacing:.5px}
  .about p{font-size:11.5px;line-height:1.5;margin-top:8px;color:var(--muted)}
  .guarantee{text-align:center;margin-top:26px}
  .guarantee h3{font-family:"Dancing Script",cursive;font-size:28px;font-weight:600}
  .guarantee svg{margin-top:8px}
  .guarantee p{font-size:11.5px;line-height:1.45;color:var(--muted);margin:8px 30px 0}
  .floor-strip{height:70px;margin-top:16px;background:linear-gradient(90deg,#5f6366,#b9bcbe 40%,#8b8f92 70%,#4f5356)}
  .cta{text-align:center;margin-top:22px;padding:0 22px}
  .cta h4{font-family:"Oswald",Arial,sans-serif;font-weight:600;font-size:25px;line-height:1.05;text-transform:uppercase;letter-spacing:.5px}
  .cta h4 .free{color:var(--blue)}
  .cta .for{color:var(--blue);font-size:10.5px;font-weight:700;text-transform:uppercase;margin-top:5px}
  .cta .also{font-size:10.5px;font-weight:700;text-transform:uppercase}
  .brand{display:flex;align-items:center;gap:10px;justify-content:center;margin-top:32px}
  .brand-square{width:30px;height:30px;background:var(--red)}
  .brand-name{font-size:15px;font-weight:700;color:var(--ink);line-height:1.1}
  .brand-tag{text-align:center;font-size:10px;color:var(--muted);margin-top:6px;line-height:1.35}
</style>
</head>
<body>
<main class="brochure">

  <section class="panel panel--blue panel--left">
    <div class="panel-copy">
      <h1 class="headline"><span class="lead"><span class="gold">GOLD STAR</span> Licensed Applicators</span><span class="serif">of Duraplex Floor Toppings</span></h1>
      <p class="body-copy">Many industrial properties throughout New Zealand require well protected, non-slip hygienic floors in order to operate.</p>
      <p class="body-copy">As licensed applicators of Duraplex Terrastone, Duthane and Terragrip etc., our team are the guys to call when you require superior floor toppings. Resin floor toppings are specialist systems that fully bond to the concrete, providing seamless, hard-wearing and anti-microbial floors (which become sterile and hygienic).</p>
      <p class="body-copy">Ideal in a variety of residential, commercial and industrial environments, resin floor toppings will help to meet any health and safety codes required by local authorities, and are becoming increasingly popular in homes given their practicality, and aesthetic qualities.</p>
      <ul class="checks">
        <li><svg viewBox="0 0 22 18"><rect x="1" y="5" width="12" height="12" fill="none" stroke="#0b2340" stroke-width="1.6"/><path d="M4 10l4 4 12-13" fill="none" stroke="#0b2340" stroke-width="2.4"/></svg>EXPERIENCE</li>
        <li><svg viewBox="0 0 22 18"><rect x="1" y="5" width="12" height="12" fill="none" stroke="#0b2340" stroke-width="1.6"/><path d="M4 10l4 4 12-13" fill="none" stroke="#0b2340" stroke-width="2.4"/></svg>QUALITY</li>
        <li><svg viewBox="0 0 22 18"><rect x="1" y="5" width="12" height="12" fill="none" stroke="#0b2340" stroke-width="1.6"/><path d="M4 10l4 4 12-13" fill="none" stroke="#0b2340" stroke-width="2.4"/></svg>VALUE</li>
      </ul>
    </div>
    <div class="social"><i></i>fb.com/tvsurfacing</div>
  </section>

  <section class="panel panel--blue panel--middle">
    <div class="panel-copy">
      <h2 class="headline--right"><span class="light">Non-Slip Coatings</span><span class="bold">AND APPLICATIONS</span></h2>
      <p class="body-copy">If you have an area in your property that requires a non-slip surface (such as a walkway, patio areas, garages, carparks, bathrooms or pool surroundings etc), talk to us at TV Surfacing Contractors.</p>
      <p class="body-copy">Our concrete systems and non-slip applications are ideal for a number of requirements, and will leave your concrete floors looking great!</p>
      <p class="options-title">Options may include:</p>
      <ul class="options">
        <li>Acid Washed Concrete and a specialised Sealant applied to protect and enhance the concrete</li>
        <li>Concrete Grinding and Sealant applied with specific non slip beads</li>
        <li>Duraplex Terrachip – decorative Flooring with Flake Finish – Seamless, safe &amp; waterproof</li>
        <li>Duraplex Gripstone – non slip flooring</li>
      </ul>
    </div>
  </section>

  <svg class="scene" width="720" height="760" viewBox="0 0 720 760">
    <defs>
      <linearGradient id="homePhoto" x1="0" y1="0" x2="0" y2="1">
        <stop offset="0" stop-color="#d3dde6"/><stop offset=".7" stop-color="#b8c6d2"/><stop offset="1" stop-color="#5d6c78"/>
      </linearGradient>
      <linearGradient id="poolPhoto" x1="0" y1="0" x2="0" y2="1">
        <stop offset="0" stop-color="#cfdae3"/><stop offset=".55" stop-color="#8fb2d0"/><stop offset="1" stop-color="#1e5fa8"/>
      </linearGradient>
    </defs>
    <polygon points="0,700 360,620 360,760 0,760" fill="url(#homePhoto)" role="img" aria-label="Photo of a modern white two-storey home with covered patio, outdoor dining set and polished concrete terrace"/>
    <polygon points="360,620 720,540 720,760 360,760" fill="url(#poolPhoto)" role="img" aria-label="Photo of a modern home beside a blue swimming pool with polished concrete surrounds"/>
    <polygon points="0,610 720,450 720,540 0,700" fill="var(--blue-band)"/>
    <line x1="360" y1="530" x2="360" y2="760" stroke="rgba(0,0,0,.15)" stroke-width="1"/>
    <text x="420" y="555" fill="#fff" font-family="Dancing Script, cursive" font-weight="600" font-size="30" transform="rotate(-12.5 420 555)">Specialist in :</text>
    <text x="250" y="629" fill="#fff" font-family="Open Sans, sans-serif" font-weight="700" font-size="11.5" letter-spacing=".3" transform="rotate(-12.5 250 629)">CONCRETE POLISHING, GRINDING AND RESIN FLOOR TOPPINGS.</text>
  </svg>

  <section class="panel panel--white panel--right">
    <div class="about">
      <h2>ABOUT US</h2>
      <p>Our New Zealand based, locally owned business has been serving Auckland for over 17 years. We are a reliable team of concrete polishing, grinding and preparation specialists, offering resin floor toppings and non-slip flooring options.</p>
    </div>
    <div class="guarantee">
      <h3>Our guarantee to you :</h3>
      <svg width="28" height="27" viewBox="0 0 28 27" aria-hidden="true"><polygon points="14,1 17.6,10 27,10 19.5,16 22.3,26 14,20 5.7,26 8.5,16 1,10 10.4,10" fill="var(--red)"/></svg>
      <p>Have complete peace of mind when dealing with us, as we provide a workmanship guarantee on all services.</p>
    </div>
    <div class="floor-strip" role="img" aria-label="Photo strip of a polished concrete floor surface"></div>
    <div class="cta">
      <h4>Arrange your <span class="free">free</span> quote<br>and consultation</h4>
      <p class="for">for concrete polishing, concrete preparation,</p>
      <p class="also">non-slip coatings or resin floor toppings</p>
    </div>
    <div class="brand">
      <span class="brand-square"></span>
      <span class="brand-name">TV Surfacing<br>Contractors</span>
    </div>
    <p class="brand-tag">Concrete Grinding &amp; Polishing<br>Industrial Resin Floors</p>
  </section>

</main>
</body>
</html>
```